New, modern business card for growing audiology practice

We need a new business card for our audiology practice. Our logo and website have recently changed (more modern) and we want our business cards to reflect this change.
We conduct hearing tests, perform earwax removals, and fit & dispense hearing aids to our patients. We are a family owned practice in which the owner is the one who works directly with the patient. I have attached logos in various formats to use, as well as two ideas I found on this website; as well as a scanned copy of our current logo. Good luck!

Industry/Entity Type

Business

Contact Information for Business Card

Company name: Maplow Hearing Center
Provider name: Peter Mulvoy, Au.D. F/ISN
Phone number: (555) 318-6042
Address: 87 W. Linden Ave. Fernhollow, OH 44391
email: maplowhearing@postvale.net
website: maplowhearing.com

Colors
000000
aaaaaa
dbdbdb
cacaca
9bcb3c
afd23c
cadf82
b1b1b1

Requirements
Must have
• My card must include information in the "details" section. In the attached images, I found a few that I liked and I would like to model after - "brisk tumblin'" and "Sound Wellness Center".
• Must be horizontal.
• Must include logos provided. I uploaded them in various file formats and various ways.
• Must match logo font, if possible, if not, please get as close as you can.
Nice to have
• I really like the idea of having a color on one side with just the logo and company name and the contact information and provider name on the other side. I also really like the idea of having the main color dominating on the logo/company side with accent of that same color on the contact side of the card.
Should not have
• Must not be vertical.

```html
<!DOCTYPE html>
<html lang="en">
<head>
<meta charset="utf-8">
<title>Maplow Hearing Center – Business Card</title>
<link href="https://fonts.googleapis.com/css2?family=Raleway:wght@400;500;600&family=Montserrat:wght@400;500&display=swap" rel="stylesheet">
<style>
  :root {
    --ink: #000000;
    --grey: #aaaaaa;
    --grey-mid: #b1b1b1;
    --paper: #ffffff;
    --canvas: #f2f2f2;
    --green: #9bcb3c;
    --green-bright: #afd23c;
    --green-light: #cadf82;
  }
  * { box-sizing: border-box; margin: 0; padding: 0; }
  html, body { width: 1200px; height: 1200px; overflow: hidden; }
  body {
    background: var(--canvas);
    font-family: "Raleway", sans-serif;
    color: var(--ink);
    position: relative;
  }
  .card {
    position: absolute;
    top: 458px;
    width: 500px;
    height: 284px;
    background: var(--paper);
    box-shadow: 0 2px 8px rgba(0,0,0,.12);
    overflow: hidden;
  }
  .card--front { left: 70px; }
  .card--back { left: 630px; }

  /* front */
  .front__head {
    height: 118px;
    display: flex;
    align-items: center;
    justify-content: center;
  }
  .wordmark {
    font-weight: 500;
    letter-spacing: -0.6px;
    white-space: nowrap;
    color: var(--ink);
  }
  .front__head .wordmark { font-size: 31px; }
  .front__body {
    height: 124px;
    background: var(--green-light);
    text-align: center;
    padding-top: 50px;
  }
  .holder__name {
    font-family: "Montserrat", sans-serif;
    font-size: 21px;
    font-weight: 500;
    letter-spacing: .3px;
  }
  .holder__title {
    font-family: "Montserrat", sans-serif;
    font-size: 16px;
    margin-top: 1px;
  }
  .front__foot {
    height: 42px;
    background: var(--green-bright);
    color: var(--paper);
    font-size: 16px;
    letter-spacing: -0.5px;
    display: flex;
    align-items: center;
    justify-content: center;
  }

  /* back */
  .back__info {
    position: absolute;
    left: 19px;
    top: 30px;
    width: 290px;
  }
  .back__info .wordmark { font-size: 20px; letter-spacing: -0.5px; }
  .provider {
    margin-top: 20px;
    font-size: 16px;
    font-weight: 500;
    letter-spacing: -0.6px;
  }
  .contacts { list-style: none; margin-top: 22px; }
  .contacts li {
    display: flex;
    align-items: flex-start;
    font-size: 15px;
    letter-spacing: -0.4px;
    color: #333;
    line-height: 29px;
    white-space: nowrap;
  }
  .contacts svg {
    width: 14px; height: 14px;
    margin: 8px 4px 0 0;
    flex: none;
    fill: var(--grey);
  }
  .contacts .indent { padding-left: 18px; }
  .back__panel {
    position: absolute;
    left: 316px;
    top: 0;
    width: 184px;
    height: 284px;
    background: var(--green);
  }
  .back__panel .dot {
    position: absolute;
    left: 32px;
    top: 82px;
    width: 120px;
    height: 120px;
    border-radius: 50%;
    background: var(--green-light);
    opacity: .55;
  }
</style>
</head>
<body>

<section class="card card--front">
  <div class="front__head">
    <span class="wordmark">MAPLOW HEARING CENTER</span>
  </div>
  <div class="front__body">
    <p class="holder__name">John D. Smith</p>
    <p class="holder__title">Title</p>
  </div>
  <div class="front__foot">Provider Peter Mulvoy, Au.D. F/ISN</div>
</section>

<section class="card card--back">
  <div class="back__info">
    <p class="wordmark">MAPLOW HEARING CENTER</p>
    <p class="provider">Provider Peter Mulvoy, Au.D. F/ISN</p>
    <ul class="contacts">
      <li>
        <svg viewBox="0 0 24 24" aria-hidden="true"><path d="M6.6 10.8a15.1 15.1 0 0 0 6.6 6.6l2.2-2.2c.3-.3.7-.4 1-.2 1.1.4 2.3.6 3.6.6.6 0 1 .4 1 1V20c0 .6-.4 1-1 1A17 17 0 0 1 3 4c0-.6.4-1 1-1h3.5c.6 0 1 .4 1 1 0 1.3.2 2.5.6 3.6.1.3 0 .7-.2 1z"/></svg>
        (555) 318-6042
      </li>
      <li>
        <svg viewBox="0 0 24 24" aria-hidden="true"><path d="M12 2a7 7 0 0 0-7 7c0 5.3 7 13 7 13s7-7.7 7-13a7 7 0 0 0-7-7zm0 9.5A2.5 2.5 0 1 1 12 6.5a2.5 2.5 0 0 1 0 5z"/></svg>
        87 W. Linden Ave. Fernhollow,
      </li>
      <li class="indent">OH 44391</li>
      <li>
        <svg viewBox="0 0 24 24" aria-hidden="true"><path d="M12 2a10 10 0 1 0 5 18.7l-.9-1.7A8 8 0 1 1 20 12v1a2 2 0 0 1-4 0V7h-2v1a5 5 0 1 0 .7 6.9A4 4 0 0 0 22 13v-1A10 10 0 0 0 12 2zm0 13a3 3 0 1 1 0-6 3 3 0 0 1 0 6z"/></svg>
        maplowhearing@postvale.net
      </li>
      <li>
        <svg viewBox="0 0 24 24" aria-hidden="true"><path d="M12 2a10 10 0 1 0 0 20 10 10 0 0 0 0-20zm6.9 6h-3a15 15 0 0 0-1.3-3.9A8 8 0 0 1 18.9 8zM12 4c.8 1.2 1.5 2.5 1.9 4h-3.8c.4-1.5 1.1-2.8 1.9-4zM4.3 14a8 8 0 0 1 0-4h3.4a16 16 0 0 0 0 4zm.8 2h3a15 15 0 0 0 1.3 3.9A8 8 0 0 1 5.1 16zm3-8h-3a8 8 0 0 1 4.3-3.9C8.8 5.3 8.4 6.6 8.1 8zM12 20c-.8-1.2-1.5-2.5-1.9-4h3.8c-.4 1.5-1.1 2.8-1.9 4zm2.3-6H9.7a14 14 0 0 1 0-4h4.6a14 14 0 0 1 0 4zm.3 5.9c.6-1.2 1-2.5 1.3-3.9h3a8 8 0 0 1-4.3 3.9zm1.7-5.9a16 16 0 0 0 0-4h3.4a8 8 0 0 1 0 4z"/></svg>
        maplowhearing.com
      </li>
    </ul>
  </div>
  <div class="back__panel">
    <span class="dot"></span>
  </div>
</section>

</body>
</html>
```